SnapMingle App Log-in Screen Design

We need a design for the main Log-in screen of an App we are developing.

The only requirement is it must have for 2 buttons called 'play' and 'register'. The rest of the screen design is up to you.

We want it to be fun and engaging and we have no preference between an animation/cartoon look or a classical photo background. Essentially we don't have a preconceived idea so no point asking us for direction... Each design will be judged on its wow factor.

Without giving too much away the core concept of the App is that guests at events can Log-in to the event through the App and take photos on their phones and these photos will be made available to the event organisers.
Updates

Designs that are jut plain screen with buttons will not be considered.  We are looking for something that engages the user... get creative!

```html
<!DOCTYPE html>
<html lang="en">
<head>
<meta charset="utf-8">
<title>SnapMingle – Log-in</title>
<link rel="stylesheet" href="https://fonts.googleapis.com/css2?family=Raleway:wght@400;500&family=Open+Sans:wght@400;600;700&display=swap">
<style>
  :root {
    --screen-black: #050608;
    --status-text: #ffffff;
    --sky-white: #f6f7fa;
    --glow-blue: #b9d3f2;
    --stage-blue: #3f86d8;
    --crowd-blue: #1b3f78;
    --field-fill: rgba(255, 255, 255, 0.72);
    --field-border: rgba(255, 255, 255, 0.95);
    --field-text: #4a5260;
    --icon-dark: #2a2d33;
    --brand-grey: #9aa1ab;
    --label-dark: #22252b;
    --login-top: #f7891f;
    --login-bottom: #e05e06;
    --button-top: #ffffff;
    --button-bottom: #c9cbcf;
    --button-text: #2f3236;
  }

  * { box-sizing: border-box; margin: 0; padding: 0; }

  html, body {
    width: 696px;
    height: 1200px;
    overflow: hidden;
    background: var(--screen-black);
  }

  .screen {
    position: relative;
    width: 696px;
    height: 1200px;
    background: var(--screen-black);
    font-family: "Open Sans", Arial, sans-serif;
  }

  .status-bar {
    position: absolute;
    left: 0; top: 0;
    width: 100%;
    height: 38px;
    background: #000;
    color: var(--status-text);
    font-weight: 700;
    font-size: 25px;
    display: flex;
    align-items: center;
    padding: 0 12px;
    z-index: 2;
  }
  .status-left, .status-right { display: flex; align-items: center; gap: 8px; flex: 1; }
  .status-right { justify-content: flex-end; gap: 12px; }
  .status-time { flex: 0 0 auto; }

  .event-backdrop {
    position: absolute;
    left: 0; top: 38px;
    width: 100%;
    height: 1012px;
    background:
      radial-gradient(ellipse 45% 22% at 60% 42%, rgba(255,255,255,0.85), rgba(255,255,255,0) 70%),
      linear-gradient(to bottom,
        var(--sky-white) 0%,
        var(--sky-white) 14%,
        var(--glow-blue) 30%,
        var(--stage-blue) 52%,
        var(--crowd-blue) 68%,
        #0b1a33 84%,
        var(--screen-black) 100%);
  }

  .brand-name {
    position: absolute;
    left: 0; top: 300px;
    width: 100%;
    text-align: center;
    font-family: "Raleway", Arial, sans-serif;
    font-weight: 500;
    font-size: 72px;
    letter-spacing: 1px;
    color: var(--brand-grey);
  }

  .field {
    position: absolute;
    left: 74px;
    width: 550px;
    height: 83px;
    border-radius: 15px;
    background: var(--field-fill);
    border: 2px solid var(--field-border);
    display: flex;
    align-items: center;
    justify-content: center;
    font-family: "Raleway", Arial, sans-serif;
    font-size: 32px;
    color: var(--field-text);
  }
  .field-icon {
    position: absolute;
    left: 36px;
    top: 50%;
    transform: translateY(-50%);
  }
  .field-username { top: 459px; }
  .field-password { top: 569px; }

  .login-options {
    position: absolute;
    top: 684px;
    left: 123px;
    right: 60px;
    height: 35px;
    display: flex;
    align-items: center;
    font-family: "Open Sans", Arial, sans-serif;
    font-size: 21px;
    color: var(--label-dark);
  }
  .checkbox {
    width: 35px; height: 35px;
    border: 2px solid #3c3f45;
    background: rgba(255,255,255,0.5);
    margin-right: 19px;
  }
  .divider {
    width: 1px; height: 40px;
    background: rgba(60,63,69,0.45);
    margin: 0 34px 0 34px;
  }

  .button {
    position: absolute;
    border-radius: 12px;
    display: flex;
    align-items: center;
    justify-content: center;
    gap: 22px;
    font-family: "Open Sans", Arial, sans-serif;
    font-weight: 600;
  }
  .button-login {
    left: 76px; top: 837px;
    width: 548px; height: 79px;
    background: linear-gradient(to bottom, var(--login-top), var(--login-bottom));
    color: #fff;
    font-size: 32px;
  }
  .button-secondary {
    top: 930px;
    height: 78px;
    background: linear-gradient(to bottom, var(--button-top), var(--button-bottom));
    color: var(--button-text);
    font-size: 30px;
  }
  .button-play { left: 76px; width: 274px; }
  .button-register { left: 360px; width: 264px; }
</style>
</head>
<body>
  <main class="screen">
    <header class="status-bar">
      <div class="status-left">
        <svg width="40" height="18" viewBox="0 0 40 18" aria-hidden="true">
          <rect x="0" y="12" width="5" height="6" fill="#fff"/>
          <rect x="8" y="9" width="5" height="9" fill="#fff"/>
          <rect x="16" y="6" width="5" height="12" fill="#fff"/>
          <rect x="24" y="3" width="5" height="15" fill="#fff"/>
          <rect x="32" y="0" width="5" height="18" fill="#777"/>
        </svg>
        <span class="carrier">Netlink</span>
        <svg width="32" height="22" viewBox="0 0 32 22" aria-hidden="true" style="margin-left:14px">
          <path d="M2 8 A20 20 0 0 1 30 8" stroke="#fff" stroke-width="3.5" fill="none"/>
          <path d="M7 13 A13 13 0 0 1 25 13" stroke="#fff" stroke-width="3.5" fill="none"/>
          <circle cx="16" cy="19" r="3" fill="#fff"/>
        </svg>
      </div>
      <span class="status-time">4:33 PM</span>
      <div class="status-right">
        <svg width="16" height="22" viewBox="0 0 16 22" aria-hidden="true">
          <path d="M2 6 L14 16 L8 21 L8 1 L14 6 L2 16" stroke="#fff" stroke-width="2.5" fill="none"/>
        </svg>
        <span>100%</span>
        <svg width="44" height="22" viewBox="0 0 44 22" aria-hidden="true">
          <rect x="1" y="1" width="38" height="20" rx="3" stroke="#fff" stroke-width="2" fill="none"/>
          <rect x="4" y="4" width="32" height="14" fill="#fff"/>
          <rect x="40" y="7" width="3" height="8" fill="#fff"/>
        </svg>
      </div>
    </header>

    <div class="event-backdrop" role="img" aria-label="Concert crowd with raised hands under bright blue stage lights"></div>

    <h1 class="brand-name">SnapMingle</h1>

    <div class="field field-username">
      <svg class="field-icon" width="46" height="48" viewBox="0 0 46 48" aria-hidden="true">
        <circle cx="23" cy="13" r="11" fill="var(--icon-dark)"/>
        <path d="M2 48 C2 32 10 27 23 27 C36 27 44 32 44 48 Z" fill="var(--icon-dark)"/>
      </svg>
      <span>Username</span>
    </div>

    <div class="field field-password">
      <svg class="field-icon" width="42" height="46" viewBox="0 0 42 46" aria-hidden="true">
        <path d="M10 20 V13 A11 11 0 0 1 32 13 V20" stroke="var(--icon-dark)" stroke-width="5" fill="none"/>
        <rect x="3" y="20" width="36" height="26" rx="3" fill="var(--icon-dark)"/>
        <circle cx="21" cy="31" r="4" fill="#fff"/>
        <rect x="19.5" y="32" width="3" height="8" fill="#fff"/>
      </svg>
      <span>Password</span>
    </div>

    <div class="login-options">
      <span class="checkbox" aria-hidden="true"></span>
      <span>Remember me</span>
      <span class="divider" aria-hidden="true"></span>
      <span>Forgot Password?</span>
    </div>

    <div class="button button-login">Login</div>

    <div class="button button-secondary button-play">
      <svg width="34" height="38" viewBox="0 0 34 38" aria-hidden="true">
        <path d="M2 2 L32 19 L2 36 Z" fill="var(--button-text)"/>
      </svg>
      <span>Play</span>
    </div>

    <div class="button button-secondary button-register">
      <svg width="42" height="40" viewBox="0 0 42 40" aria-hidden="true">
        <path d="M24 6 H4 V36 H34 V18" stroke="var(--button-text)" stroke-width="4" fill="none"/>
        <path d="M14 26 L16 19 L33 2 L39 8 L22 25 Z" fill="var(--button-text)"/>
      </svg>
      <span>Register</span>
    </div>
  </main>
</body>
</html>
```